We are a physical therapy billing company. We need a postcard style flyer.

See attached. We are trying to generate more business for our physical therapy billing company. Our company name is Stridewell Claims Partners.

Industry/Entity Type

Physical Therapy

```html
<!DOCTYPE html>
<html lang="en">
<head>
<meta charset="utf-8">
<title>Stridewell Claims Partners – Postcard Flyer</title>
<link href="https://fonts.googleapis.com/css2?family=Alegreya+Sans:wght@400;500;700&family=Encode+Sans+Condensed:wght@600&display=swap" rel="stylesheet">
<style>
  :root {
    --page-bg: #eeeae4;
    --card-white: #ffffff;
    --brand-blue: #1f7fc4;
    --brand-green: #3fae49;
    --photo-teal: #2aa3d3;
    --photo-light: #f4f6f7;
    --ink: #1c1c24;
    --back-top: #ffffff;
    --back-bottom: #5a8ed2;
  }
  * { box-sizing: border-box; margin: 0; padding: 0; }
  html, body { width: 1200px; height: 1187px; overflow: hidden; }
  body {
    position: relative;
    background: var(--page-bg);
    font-family: "Alegreya Sans", sans-serif;
    color: var(--ink);
  }
  .card {
    position: absolute;
    width: 700px;
    height: 540px;
    overflow: hidden;
  }
  .card-front { left: 31px; top: 28px; background: var(--card-white); }
  .front-header {
    height: 184px;
    display: flex;
    align-items: center;
    padding-left: 38px;
    gap: 30px;
  }
  .brand-dot {
    width: 74px; height: 74px;
    border-radius: 50%;
    background: var(--brand-green);
    flex: none;
  }
  .brand-name {
    font-family: "Encode Sans Condensed", sans-serif;
    font-weight: 600;
    font-size: 34px;
    letter-spacing: -0.8px;
    color: var(--brand-blue);
    text-transform: uppercase;
    white-space: nowrap;
  }
  .front-photo {
    height: 356px;
    background: linear-gradient(180deg, var(--photo-light) 0%, var(--photo-light) 45%, var(--photo-teal) 100%);
  }
  .card-back {
    left: 444px; top: 608px;
    background: linear-gradient(180deg, var(--back-top) 8%, var(--back-bottom) 100%);
    padding: 24px 18px 0 35px;
  }
  .back-heading {
    font-weight: 700;
    font-size: 16px;
    line-height: 20px;
  }
  .back-text {
    font-size: 13px;
    line-height: 23px;
    white-space: nowrap;
  }
  .intro { margin-bottom: 12px; }
  .why { margin-bottom: 6px; }
  .point { margin-bottom: 10px; }
  .point-label { font-weight: 700; letter-spacing: 0.2px; }
  .contact {
    margin-top: 18px;
    font-weight: 700;
    font-size: 18.5px;
    white-space: nowrap;
  }
</style>
</head>
<body>
  <section class="card card-front">
    <header class="front-header">
      <span class="brand-dot"></span>
      <h1 class="brand-name">Stridewell Claims Partners</h1>
    </header>
    <div class="front-photo" role="img" aria-label="Photo of four smiling clinicians in scrubs and white coats with stethoscopes"></div>
  </section>

  <section class="card card-back">
    <h2 class="back-heading">Billing issues?</h2>
    <p class="back-text intro">Let stridewell claims partners relieve those headaches.<br>
    We guarantee an increase in your collections and a decrease in your accounts receivable.</p>

    <h2 class="back-heading why">Why SCP?</h2>
    <p class="back-text point"><span class="point-label">KNOWLEDGE</span> - our billers are trained exclusively in physical therapy billing and collections.<br>
    Scp will work with the billing system you choose or are currently using. In addition, with one of our<br>
    owners being a physical therapist herself, scp has first-hand knowledge in choosing a pt software program<br>
    that meets documentation standards and maximizes your collections.</p>

    <p class="back-text point"><span class="point-label">EXPERIENCE</span> - scp is a physical therapy billing and consulting company with over 25 years of experience<br>
    in managing physical therapy practices. We are experts in documentation and coding practices,<br>
    and our billers are trained in medicare and private payer guidelines and modifiers.<br>
    Scp has the skills necessary to increase the efficiency and profitability of your clinic by taking the stress<br>
    of billing and collections away from your staff, and allowing them to do what they do best – take care<br>
    of patients!</p>

    <p class="back-text point"><span class="point-label">ANCILLARY INCOME</span> - scp can also improve your revenue by showing you how to develop additional<br>
    services beyond standard physical therapy. We can develop a bracing and custom orthotics program<br>
    for your clinic that enhances patient care and provides additional sources of revenue in a competitive<br>
    marketplace.</p>

    <p class="contact">Contact SCP today at stridewellclaimspartners.com or call 301-555-0148</p>
  </section>
</body>
</html>
```